Design for a completely new online shop, selling spices -- 2

Ich benötige das Design für einen komplett neuen Online - Shop. Ich möchte in dem Shop Gewürze, Salz, Pfeffer, Zucker, Gewürzstreuer und BonBons verkaufen. Das Design soll hochwertig und elegant sein. Ich benötige die Startseite, Kategorien seiten, Produkt - Detailseite sowie Warenkorb und Checkout.

I need the design for a completely new online - shop. I want to sell in the shop spices, salt, pepper, sugar, spice shaker and Bon Bons. The design should be of high quality and elegant. I need the home page, category pages, product - Detail page and shopping cart and checkout.

```html
<!DOCTYPE html>
<html lang="de">
<head>
<meta charset="utf-8">
<title>Goldene Prise – Gewürze Online-Shop</title>
<link href="https://fonts.googleapis.com/css2?family=Lato:wght@300;400&family=Lora:wght@400&display=swap" rel="stylesheet">
<style>
  :root {
    --nav-green: #8cbf5c;
    --nav-active: #6e9e3f;
    --brown: #8a6d3b;
    --brown-text: #8b6b45;
    --line: #b89a7a;
    --price: #f2a55a;
    --grey: #777;
    --red: #b8322a;
    --white: #fff;
  }
  * { margin: 0; padding: 0; box-sizing: border-box; }
  html, body { width: 1083px; height: 1200px; overflow: hidden; background: var(--white); }
  body { position: relative; font-family: "Lato", sans-serif; color: var(--grey); }
  .abs { position: absolute; }

  .header-line { left: 0; width: 1083px; height: 1px; background: var(--line); }
  .spoon { width: 36px; height: 50px; border-radius: 50%; top: 6px; }
  .brand { left: 462px; top: 0; width: 156px; height: 146px; background: var(--white);
    display: flex; align-items: center; justify-content: center; text-align: center;
    font-family: "Lora", serif; font-size: 26px; line-height: 1.05; color: var(--red); letter-spacing: 1px; }
  .nav a { position: absolute; top: 85px; transform: translateX(-50%); font-size: 16px;
    color: var(--nav-green); text-decoration: none; text-transform: uppercase; white-space: nowrap; }
  .nav a.active { color: var(--nav-active); }

  .hero-side { top: 124px; height: 233px; width: 1083px; left: 0;
    background: linear-gradient(90deg, #7a5a35, #b58c5a 50%, #6a4a2a); opacity: .55; }
  .hero { left: 108px; top: 124px; width: 864px; height: 233px;
    background: linear-gradient(100deg, #a98354 0%, #c48a5e 25%, #8a5d3a 55%, #4a3220 100%); }
  .hero-title { right: 131px; top: 200px; text-align: right; font-family: "Lora", serif;
    font-size: 38px; line-height: 39px; color: var(--white); font-weight: 400; }
  .hero-cta { left: 760px; top: 291px; width: 190px; height: 36px; background: var(--white);
    border-radius: 3px; font-size: 19px; color: #555; display: flex; align-items: center; justify-content: center; gap: 10px; }

  .category { width: 160px; transform: translateX(-50%); top: 420px; text-align: center; }
  .category .thumb { height: 100px; margin: 0 auto; width: 150px; border-radius: 50%; }
  .category span { display: block; margin-top: 34px; font-size: 18px; font-weight: 300; color: #666; }

  .section-title { left: 108px; top: 626px; font-family: "Lora", serif; font-size: 21px;
    color: var(--brown-text); text-transform: uppercase; font-weight: 400; }

  .product { top: 674px; width: 136px; }
  .product .photo { width: 136px; height: 136px; border: 1px solid #c9a98a; position: relative; overflow: hidden; }
  .product .photo .fill { position: absolute; inset: 3px; }
  .product .badge { position: absolute; left: 0; top: 0; width: 40px; height: 40px;
    background: linear-gradient(135deg, #9a7a55 50%, transparent 50%); }
  .product h3 { margin-top: 5px; font-size: 21px; font-weight: 300; color: var(--brown-text); white-space: nowrap; overflow: hidden; text-overflow: ellipsis; }
  .product p { font-size: 11.5px; line-height: 15px; color: #777; }
  .product .price { margin-top: 9px; font-size: 29px; font-weight: 300; color: var(--price); }
  .product .buy { margin-top: 6px; height: 30px; background: var(--brown); color: var(--white);
    font-size: 14px; display: flex; align-items: center; justify-content: center; }

  .footer-nav a { position: absolute; font-size: 13.5px; color: var(--brown-text); text-decoration: none; text-transform: uppercase; }
  .footer-nav a.active { color: #6b5230; }
  .social { width: 42px; height: 42px; border-radius: 50%; background: var(--brown); top: 1055px; }
  .domain { left: 810px; top: 1062px; font-family: "Lora", serif; font-size: 26px; color: var(--brown-text); }
  .copyright { left: 112px; top: 1158px; font-family: "Lora", serif; font-size: 13px; color: #888; }
</style>
</head>
<body>
  <header>
    <div class="abs spoon" style="left:366px;background:#6e7a3a" role="img" aria-label="Löffel mit grünem Gewürz"></div>
    <div class="abs spoon" style="left:409px;background:#a93a22" role="img" aria-label="Löffel mit Paprikapulver"></div>
    <div class="abs spoon" style="left:623px;background:#d4b07a" role="img" aria-label="Löffel mit hellem Gewürz"></div>
    <div class="abs spoon" style="left:668px;background:#a8a85a" role="img" aria-label="Löffel mit Currypulver"></div>
    <div class="abs header-line" style="top:72px"></div>
    <div class="abs header-line" style="top:124px"></div>
    <nav class="nav">
      <a class="active" style="left:184px">Home</a>
      <a style="left:279px">Über uns</a>
      <a style="left:389px">Produckte</a>
      <a style="left:693px">Warenkorb</a>
      <a style="left:816px">Checkout</a>
      <a style="left:930px">Kontakte</a>
    </nav>
    <div class="abs brand">GOLDENE<br>PRISE</div>
  </header>

  <section>
    <div class="abs hero-side"></div>
    <div class="abs hero" role="img" aria-label="Gewürzmarkt mit offenen Säcken voller Pfeffer und Gewürze"></div>
    <h1 class="abs hero-title">Finden Sie alles,<br>was Sie an einem Platz</h1>
    <div class="abs hero-cta">jetzt einkaufen!
      <svg width="22" height="20" viewBox="0 0 22 20" fill="none" stroke="#555" stroke-width="2"><path d="M1 2h4l3 11h10l3-8H7"/><circle cx="9" cy="17" r="1.6" fill="#555"/><circle cx="17" cy="17" r="1.6" fill="#555"/></svg>
    </div>
  </section>

  <section class="categories">
    <div class="abs category" style="left:184px"><div class="thumb" style="background:linear-gradient(135deg,#7a3a28,#b07a4a 50%,#6a5a30)" role="img" aria-label="Bunte Pfefferkörner"></div><span>Gewürze</span></div>
    <div class="abs category" style="left:377px"><div class="thumb" style="background:linear-gradient(180deg,#dbe4ee,#aebccb)" role="img" aria-label="Salzhaufen"></div><span>Salz</span></div>
    <div class="abs category" style="left:568px"><div class="thumb" style="background:linear-gradient(135deg,#3a2a2a,#5a3a36)" role="img" aria-label="Schwarze Pfefferkörner"></div><span>Pfeffer</span></div>
    <div class="abs category" style="left:738px"><div class="thumb" style="background:linear-gradient(180deg,#ececec,#bdbdbd)" role="img" aria-label="Zuckerwürfel"></div><span>Zucker</span></div>
    <div class="abs category" style="left:906px"><div class="thumb" style="background:linear-gradient(135deg,#d9a870,#a06a38)" role="img" aria-label="Pfeffermühle und Mörser aus Holz"></div><span>Gewürzstreuer</span></div>
  </section>

  <section>
    <h2 class="abs section-title">Unsere Verkaufsschlager</h2>
    <article class="abs product" style="left:108px">
      <div class="photo"><div class="fill" style="background:linear-gradient(180deg,#9a9a9a,#d8d8d8 45%,#c4c4c4)" role="img" aria-label="Salzstreuer"></div></div>
      <h3>Weiß Salzs</h3><p>Perfekt für rotes Fleisch und Huhn</p><div class="price">€7.99</div><div class="buy">jetzt kaufen</div>
    </article>
    <article class="abs product" style="left:291px">
      <div class="photo"><div class="fill" style="background:linear-gradient(180deg,#8e8e8e,#d2d2d2 45%,#bcbcbc)" role="img" aria-label="Meersalzstreuer aus Glas"></div><div class="badge"></div>
        <svg class="abs" style="left:0;top:0" width="40" height="40"><text x="7" y="24" transform="rotate(-45 14 18)" font-family="Lato, sans-serif" font-size="10" fill="#fff">NEU</text></svg></div>
      <h3>Meersalz</h3><p>Perfekt für rotes Fleisch und Huhn</p><div class="price">€7.99</div><div class="buy">jetzt kaufen</div>
    </article>
    <article class="abs product" style="left:474px">
      <div class="photo"><div class="fill" style="background:radial-gradient(#c89a70,#7a5030)" role="img" aria-label="Muskatnuss"></div></div>
      <h3>Gałka muszkatołowa</h3><p>Perfekt für rotes Fleisch und Huhn</p><div class="price">€7.99</div><div class="buy">jetzt kaufen</div>
    </article>
    <article class="abs product" style="left:657px">
      <div class="photo"><div class="fill" style="background:radial-gradient(#6a3a25,#a0765a)" role="img" aria-label="Getrocknete Nelken"></div></div>
      <h3>Zimt</h3><p>Perfekt für rotes Fleisch und Huhn</p><div class="price">€7.99</div><div class="buy">jetzt kaufen</div>
    </article>
    <article class="abs product" style="left:839px">
      <div class="photo"><div class="fill" style="background:radial-gradient(#6aa838,#bfe08a)" role="img" aria-label="Pfefferminzblätter"></div></div>
      <h3>Pfefferminze</h3><p>Perfekt für rotes Fleisch und Huhn</p><div class="price">€7.99</div><div class="buy">jetzt kaufen</div>
    </article>
  </section>

  <footer>
    <div class="abs header-line" style="top:1002px"></div>
    <div class="abs header-line" style="top:1029px"></div>
    <nav class="footer-nav">
      <a class="active" style="left:108px;top:1051px">Home</a>
      <a style="left:108px;top:1071px">Über uns</a>
      <a style="left:108px;top:1093px">Kontakte</a>
      <a style="left:255px;top:1051px">Produckte</a>
      <a style="left:255px;top:1071px">Warenkorb</a>
      <a style="left:255px;top:1093px">Checkout</a>
    </nav>
    <div class="abs social" style="left:690px" aria-label="Soziales Netzwerk"></div>
    <div class="abs social" style="left:738px" aria-label="Soziales Netzwerk"></div>
    <div class="abs domain">goldeneprise.de</div>
    <div class="abs copyright">goldeneprise.de &nbsp;all rights reserved 2015 ®</div>
  </footer>
</body>
</html>
```